Wine Label for Wasotane Vineyards

I grow my own grapes and make my own wine. I do this just as a hobby and do not sell any wine. I just make it for my own use and to give as gifts. I still endeavor to make the bottle look like a genuine retail bottle, so I need a professional looking label.

Harrow Peak is a state park in North Carolina. My vineyard is at the base of the mountain. Wasotane is the name the Indians called the mountain. It means "great guide" as they used the mountain as a landmark in their travels.

Need front and back label. Attached is a picture that I currently use. The new labels should contain all the language on the current label.

Size of label flexible as long as it is a standard size label, that can be easily found.

I think Harrow Peak image should be included, maybe stylized. I am looking for something for earthy, rustic and clean.

The varieties will be Pinot Noir, Cabernet Sauvignon, Carbernet Franc, Chardonnay, and Viognier. I guess all the labels would be the same, just the name would change, Unless someone has a better idea.

Target Market(s)

wine drinker

Requirements
Must have
• harrow peak image of some sort,
• front and back label
Nice to have
• Clean, earthy, rustic - the label should feel like the mountain look, even romantic

```html
<!DOCTYPE html>
<html lang="en">
<head>
<meta charset="utf-8">
<title>Wasotane Vineyards – Pinot Noir Label</title>
<link rel="stylesheet" href="https://fonts.googleapis.com/css2?family=Montserrat:wght@400;500&family=Italianno&display=swap">
<style>
  :root {
    --backdrop: #ececec;
    --label-paper: #ffffff;
    --band-black: #000000;
    --band-text: #ffffff;
    --scene-light: #ececec;
    --scene-mid: #d6d6d6;
    --type-grey: #8e8e8e;
    --script-grey: #9a9a9a;
    --varietal-red: #9b1c2a;
  }
  * { margin: 0; padding: 0; box-sizing: border-box; }
  html, body {
    width: 1200px;
    height: 1121px;
    overflow: hidden;
    background: var(--backdrop);
  }
  .canvas {
    position: relative;
    width: 1200px;
    height: 1121px;
  }
  .wine-label {
    position: absolute;
    left: 398px;
    top: 40px;
    width: 403px;
    height: 1040px;
    background: var(--label-paper);
    box-shadow: 0 2px 10px rgba(0,0,0,0.06);
  }
  .landscape-art {
    position: absolute;
    left: 0;
    top: 14px;
    width: 100%;
    height: 322px;
    background: linear-gradient(180deg, var(--scene-light) 0%, var(--scene-mid) 55%, var(--scene-light) 100%);
  }
  .name-band {
    position: absolute;
    left: -22px;
    top: 356px;
    width: 447px;
    height: 81px;
    background: var(--band-black);
    display: flex;
    align-items: center;
    justify-content: center;
  }
  .name-band .winery-name {
    font-family: 'Montserrat', sans-serif;
    font-weight: 500;
    font-size: 42px;
    letter-spacing: 0.2em;
    color: var(--band-text);
    padding-left: 0.2em;
  }
  .winery-subtitle {
    position: absolute;
    top: 472px;
    width: 100%;
    text-align: center;
    font-family: 'Italianno', cursive;
    font-size: 54px;
    line-height: 1;
    color: var(--script-grey);
  }
  .varietal {
    position: absolute;
    top: 716px;
    width: 100%;
    text-align: center;
    font-family: 'Montserrat', sans-serif;
    font-weight: 500;
    font-size: 24px;
    letter-spacing: 0.05em;
    color: var(--varietal-red);
  }
  .vintage {
    position: absolute;
    top: 920px;
    width: 100%;
    text-align: center;
    font-family: 'Montserrat', sans-serif;
    font-size: 28px;
    letter-spacing: 0.55em;
    padding-left: 0.55em;
    color: var(--type-grey);
  }
  .region {
    position: absolute;
    top: 967px;
    width: 100%;
    text-align: center;
    font-family: 'Montserrat', sans-serif;
    font-size: 15px;
    letter-spacing: 0.02em;
    color: var(--type-grey);
  }
  .appellation {
    position: absolute;
    top: 1005px;
    width: 100%;
    text-align: center;
    font-family: 'Montserrat', sans-serif;
    font-size: 14.5px;
    letter-spacing: 0.12em;
    color: var(--type-grey);
  }
</style>
</head>
<body>
<main class="canvas">
  <section class="wine-label">
    <div class="landscape-art" role="img" aria-label="Stylized grey landscape of Harrow Peak above rolling vineyard rows, with a tree on the left"></div>
    <div class="name-band">
      <span class="winery-name">WASOTANE</span>
    </div>
    <p class="winery-subtitle">Vineyards</p>
    <p class="varietal">PINOT NOIR</p>
    <p class="vintage">2014</p>
    <p class="region">NORTH CAROLINA</p>
    <p class="appellation">HARROW PEAK STATE PARK VALLEY</p>
  </section>
</main>
</body>
</html>
```